Brightwater Essence colloidal silver spray for pets.

We need a label for an 8-oz cobalt blue spray bottle. We are a small company just starting to share the benefits of colloidal silver. Our first offering will be the 8-oz spray bottle for pets. We would also like to update our logo. The finished project should be crisp and incorporate a dog on the label. I have attached the information we would like on the label and our logo, which can be changed to match your vision.
Updates

Hi, I would like to remind you that we are using a cobalt blue bottle with a black sprayer and would like an updated logo. Also, for the business cards, we don't want an animal on them, as we are planning future products for people. thank you

```html
<!DOCTYPE html>
<html lang="en">
<head>
<meta charset="utf-8">
<title>Brightwater Essence – Colloidal Silver Pet Spray Label</title>
<link rel="stylesheet" href="https://fonts.googleapis.com/css2?family=Lexend:wght@300;400;500&display=swap">
<style>
  :root {
    --bg: #f1f1f0;
    --label-white: #ffffff;
    --brand-green: #52a44c;
    --bar-navy: #1a2a9c;
    --ink-navy: #24206a;
    --dog-blue: #4157a8;
    --dog-light: #6f86c6;
    --haze: #e4e9f6;
    --flag-red: #e0262b;
  }
  * { margin: 0; padding: 0; box-sizing: border-box; }
  html, body {
    width: 1200px; height: 900px; overflow: hidden;
    background: var(--bg);
    font-family: "Lexend", sans-serif;
  }
  .label {
    position: absolute; left: 361px; top: 40px;
    width: 477px; height: 820px;
    background: var(--label-white);
    border-radius: 0 81px 81px 81px;
    overflow: hidden;
    box-shadow: 0 6px 18px rgba(0,0,0,0.18);
  }
  .brand {
    position: absolute; left: 20px; top: 120px; width: 200px;
    text-align: center; color: var(--brand-green);
    font-weight: 400; font-size: 27px; line-height: 31px; letter-spacing: 0.5px;
  }
  .brand-dot {
    display: block; width: 22px; height: 22px; margin: 0 auto 18px;
    border-radius: 50%; background: var(--brand-green);
  }
  .product-type {
    position: absolute; left: 0; top: 276px; width: 190px;
    padding-bottom: 3px; text-align: right;
    border-bottom: 1.5px solid var(--ink-navy);
    color: var(--ink-navy); font-size: 17px; font-weight: 400;
  }
  .claim-box {
    position: absolute; left: 305px; top: 27px; width: 149px; height: 154px;
    background: var(--brand-green); border-radius: 0 40px 0 0;
    color: #fff; font-size: 18px; line-height: 24px; font-weight: 400;
    padding: 44px 0 0 24px; letter-spacing: 0.3px;
  }
  .spec-bar {
    position: absolute; left: 305px; width: 172px; height: 25px;
    background: var(--bar-navy); color: #fff;
    font-size: 17px; line-height: 26px; font-weight: 400; text-align: center;
  }
  .spec-bar.ppm { top: 213px; }
  .spec-bar.pure { top: 256px; }
  .spec-bar.preservatives { top: 300px; }
  .spec-bar.additives { top: 343px; }
  .dog-illustration {
    position: absolute; left: 0; top: 380px; width: 477px; height: 360px;
    background: linear-gradient(160deg, var(--haze) 0%, #ffffff 35%, var(--dog-light) 55%, var(--dog-blue) 80%);
  }
  .origin {
    position: absolute; left: 18px; top: 654px; width: 64px;
    text-align: center; color: var(--ink-navy);
    font-size: 12.5px; line-height: 14px; letter-spacing: 0.3px;
  }
  .origin-flag {
    display: block; width: 54px; height: 25px; margin: 3px auto;
    background: linear-gradient(90deg, var(--flag-red) 0 25%, #fff 25% 75%, var(--flag-red) 75%);
  }
  .benefit-band {
    position: absolute; left: 0; top: 720px; width: 477px; height: 100px;
    background: var(--brand-green);
    clip-path: polygon(0 4px, 100% 18px, 100% 100%, 0 100%);
    color: #fff; text-align: center;
    font-size: 15px; line-height: 21px; font-weight: 400; letter-spacing: 0.2px;
    padding-top: 32px;
  }
</style>
</head>
<body>
  <main class="label">
    <div class="brand"><span class="brand-dot"></span>BRIGHTWATER<br>ESSENCE</div>
    <div class="product-type">Colloidal Silver</div>

    <div class="claim-box">NATURAL<br>FIRST AID<br>FOR PETS</div>
    <div class="spec-bar ppm">10 PPM</div>
    <div class="spec-bar pure">100% pure</div>
    <div class="spec-bar preservatives">No preservatives</div>
    <div class="spec-bar additives">No additives</div>

    <div class="dog-illustration" role="img" aria-label="Flat illustration of a seated blue dog in profile on a pale background"></div>

    <div class="origin">MADE IN<span class="origin-flag" role="img" aria-label="Canadian flag"></span>CANADA</div>

    <div class="benefit-band">
      Anti microbial, Anti Fungal, Anti Bacterial, Anti Viral<br>
      Treats burns, bites,cuts, abrasions, hots spots
    </div>
  </main>
</body>
</html>
```